New Zealand Luggage Importer Needs Business Cards

We need professional, creative and fashionable business cards created.
We are based in New Zealand and import and distribute high-end, quality, fashionable and durable luggage.
We pride ourselves on selling the very best quality luggage, second only to 1 brand (which we won't mention here)...we use the same manufacturer. However, our prices are much more reasonable.
Industry/Entity Type
Business
Contact Information for Business Card
Mark Dunsley
027 512 4068
3/17 Harlow Street, Pinecrest Flats, Auckland, 0614
PO Box 204377, Fernside, Auckland 0731
09-528-3916
sales@brivancases.co.nz / www.brivancases.co.nz

```html
<!DOCTYPE html>
<html lang="en">
<head>
<meta charset="utf-8">
<title>Brivan Cases – Business Card</title>
<link href="https://fonts.googleapis.com/css2?family=Open+Sans:wght@400;600;700&display=swap" rel="stylesheet">
<style>
  :root {
    --backdrop: #5a4939;
    --charcoal: #231f20;
    --white: #ffffff;
    --gold: #c9a257;
    --gold-light: #e6c27a;
    --gold-dark: #9c7433;
    --ink: #2a2420;
  }
  * { box-sizing: border-box; margin: 0; padding: 0; }
  html, body { width: 1200px; height: 987px; overflow: hidden; }
  body {
    background: var(--backdrop);
    font-family: "Open Sans", sans-serif;
    position: relative;
  }
  .card {
    position: absolute;
    left: 293px;
    width: 615px;
    height: 350px;
    overflow: hidden;
    box-shadow: 0 3px 8px rgba(0,0,0,0.35);
  }
  .card--front { top: 130px; background: var(--white); }
  .card--back { top: 505px; background: var(--charcoal); }

  .wordmark {
    position: absolute;
    left: 0; right: 0;
    text-align: center;
    font-weight: 700;
    line-height: 1;
    white-space: nowrap;
  }
  .card--front .wordmark { top: 63px; font-size: 38px; letter-spacing: 3px; color: var(--charcoal); }
  .card--back .wordmark { top: 140px; font-size: 44px; letter-spacing: 4px; color: var(--white); }

  .name-band {
    position: absolute;
    top: 170px; left: 0; right: 0;
    height: 63px;
    background: var(--charcoal);
    text-align: center;
    padding-top: 8px;
  }
  .name-band .person { color: var(--gold); font-size: 22px; font-weight: 600; line-height: 1.1; }
  .name-band .role { color: var(--white); font-size: 16px; line-height: 1.2; }

  .contact-band {
    position: absolute;
    top: 233px; left: 0; right: 0; bottom: 0;
    background: linear-gradient(90deg, var(--gold-dark) 0%, var(--gold-light) 50%, var(--gold-dark) 100%);
    text-align: center;
    color: var(--ink);
    font-size: 15px;
    line-height: 24px;
    padding-top: 8px;
  }
  .contact-row { display: flex; justify-content: center; align-items: center; gap: 6px; margin-top: 4px; }
  .contact-row + .contact-row { margin-top: 0; }
  .contact-row svg { width: 13px; height: 13px; fill: var(--ink); flex: none; }
  .contact-row .item { display: inline-flex; align-items: center; gap: 4px; }

  .tagline {
    position: absolute;
    top: 188px; left: 0; right: 0;
    text-align: center;
    font-size: 17px;
    line-height: 1.2;
    font-weight: 700;
    color: var(--white);
    letter-spacing: 0.3px;
    white-space: nowrap;
  }
  .tagline .accent { color: var(--gold-light); }

  .warranty-seal {
    position: absolute;
    top: 30px; left: 502px;
    width: 84px; height: 84px;
    border-radius: 50%;
    background: radial-gradient(circle at 40% 35%, var(--gold-light), var(--gold-dark));
  }

  .social-row {
    position: absolute;
    top: 283px; left: 0; right: 0;
    display: flex; justify-content: center; align-items: center; gap: 4px;
  }
  .social-row .rule { width: 58px; height: 2px; background: linear-gradient(90deg, transparent, #9a9a9a); }
  .social-row .rule--right { background: linear-gradient(90deg, #9a9a9a, transparent); }
  .social-row .dot {
    width: 30px; height: 30px; border-radius: 50%;
    background: radial-gradient(circle at 40% 35%, var(--gold-light), var(--gold-dark));
  }
</style>
</head>
<body>
  <section class="card card--front">
    <div class="wordmark">BRIVAN CASES</div>
    <div class="name-band">
      <div class="person">MARK DUNSLEY</div>
      <div class="role">Founder</div>
    </div>
    <div class="contact-band">
      <div>3/17 Harlow Street, Pinecrest Flats, Auckland, 0614</div>
      <div>PO Box 204377, Fernside, Auckland 0731</div>
      <div class="contact-row">
        <span class="item">
          <svg viewBox="0 0 24 24" aria-hidden="true"><path d="M6.6 10.8a15.1 15.1 0 0 0 6.6 6.6l2.2-2.2c.3-.3.7-.4 1-.2 1.1.4 2.3.6 3.6.6.6 0 1 .4 1 1V20c0 .6-.4 1-1 1A17 17 0 0 1 3 4c0-.6.4-1 1-1h3.5c.6 0 1 .4 1 1 0 1.3.2 2.5.6 3.6.1.3 0 .7-.2 1z"/></svg>
          09-528-3916
        </span>
        <span class="item">
          <svg viewBox="0 0 24 24" aria-hidden="true"><path d="M7 1h10a2 2 0 0 1 2 2v18a2 2 0 0 1-2 2H7a2 2 0 0 1-2-2V3a2 2 0 0 1 2-2zm0 3v14h10V4z"/></svg>
          027 512 4068
        </span>
      </div>
      <div class="contact-row">
        <span class="item">
          <svg viewBox="0 0 24 24" aria-hidden="true"><path d="M2 5h20v14H2zm2 2v.5l8 5 8-5V7l-8 5z"/></svg>
          sales@brivancases.co.nz
        </span>
        <span class="item">
          <svg viewBox="0 0 24 24" aria-hidden="true"><circle cx="12" cy="12" r="10"/></svg>
          www.brivancases.co.nz
        </span>
      </div>
    </div>
  </section>

  <section class="card card--back">
    <div class="warranty-seal" role="img" aria-label="Warranty seal"></div>
    <div class="wordmark">BRIVAN CASES</div>
    <div class="tagline"><span class="accent">TRUSTED</span> CASES FOR <span class="accent">TRUSTED</span> JOURNEYS</div>
    <div class="social-row">
      <span class="rule"></span>
      <span class="dot" role="img" aria-label="Social profile"></span>
      <span class="dot" role="img" aria-label="Social profile"></span>
      <span class="rule rule--right"></span>
    </div>
  </section>
</body>
</html>
```